Basic / Quick Business Card

Quick easy design project!

Need a one sided basic business card that matches font & style of brand and bottle label for our gourmet condiment, Velvet Corwin Sauce. Velvet Corwin Sauce is sold in specialty retail, gourmet groceries and appears on chef-driven restaurant menus, so the target market is a high end, gourmet, artisan-made food-loving customer.

Files Included:
Sauce Bottle Label
Velvet Corwin Sauce Round Logos

**About the logos - the logo may be used in a circle or alone vertically as on side of the bottle label**

Layout of Card:
May be vertical or horizontal based on designer ideas.

Logo usage (in circle vs. stand alone vertical logo) is up to designers descretion as well.

Reverse side of business card will be various high end / professional product photos / food shots using us.zelk.com system. **Designer on this project will NOT design a reserve for the card.**

Paper that will be used for printing:
Zelk Classic - it's a WHITE paper, but we use a cream background on Velvet Corwin Sauce branding, so please take this into account on design to stay brand consistent.

Elements & Copy for Card:
1. Logo in either script horizontal or vertical version
2. Copy: "Artisan Made - Small Batch"
3. Name - Rory Whitlock
4. Title - Creator
5. Phone - xxx.xxx.xxxx
6. xxxx@velvetcorwin.com
7. URL: velvetcorwinsauce.com
8. Social Media: @getvelvetcorwin on Twitter / Facebook / Instagram

Please provide final files in Illustrator or InDesign format.

```html
<!DOCTYPE html>
<html lang="en">
<head>
<meta charset="utf-8">
<title>Velvet Corwin Sauce – Business Card</title>
<link rel="stylesheet" href="https://fonts.googleapis.com/css2?family=Signika:wght@400;500&family=Tinos&display=swap">
<style>
  :root {
    --page: #e8e4dc;
    --card-dark: #2c2a2b;
    --brand-yellow: #f0b514;
    --white: #ffffff;
    --ink: #2c2a2b;
    --icon-muted: #8a8a8a;
  }
  * { box-sizing: border-box; margin: 0; padding: 0; }
  html, body {
    width: 869px; height: 1200px; overflow: hidden;
    background: var(--page);
  }
  .card {
    position: absolute; left: 116px; top: 40px;
    width: 637px; height: 1120px;
    background: var(--card-dark);
    font-family: "Signika", sans-serif;
    color: var(--white);
    overflow: hidden;
  }
  .top-band { position: absolute; left: 0; top: 0; width: 100%; height: 140px; background: var(--brand-yellow); }
  .top-rule { position: absolute; left: 0; top: 149px; width: 100%; height: 10px; background: var(--brand-yellow); }
  .logo-badge {
    position: absolute; left: 154px; top: 42px;
    width: 328px; height: 328px; border-radius: 50%;
    background: var(--white);
    display: flex; align-items: center; justify-content: center;
    text-align: center;
  }
  .logo-name {
    font-family: "Signika", sans-serif; font-weight: 500;
    font-size: 44px; line-height: 1.1; color: var(--ink);
  }
  .tagline {
    position: absolute; top: 364px; width: 100%; text-align: center;
    font-family: "Tinos", serif; font-size: 30px;
  }
  .contact-name {
    position: absolute; top: 666px; width: 100%; text-align: center;
    font-size: 40px; font-weight: 500;
  }
  .contact-name .title { font-size: 31px; font-weight: 400; }
  .name-underline { position: absolute; left: 212px; top: 720px; }
  .contact-line {
    position: absolute; width: 100%; text-align: center;
    display: flex; justify-content: center; align-items: center; gap: 10px;
  }
  .phone { top: 808px; font-size: 34px; }
  .email { top: 860px; font-size: 32px; }
  .social {
    position: absolute; top: 968px; width: 100%;
    display: flex; justify-content: center; align-items: center; gap: 12px;
    font-size: 30px;
  }
  .social-dots { display: flex; gap: 10px; margin-left: 6px; }
  .social-dot { width: 30px; height: 30px; border-radius: 50%; background: var(--icon-muted); }
  .bottom-band {
    position: absolute; left: 0; top: 1037px; width: 100%; height: 83px;
    background: var(--brand-yellow);
    display: flex; align-items: center; justify-content: center;
    font-size: 34px; font-weight: 500;
  }
</style>
</head>
<body>
  <main class="card">
    <div class="top-band"></div>
    <div class="top-rule"></div>
    <div class="logo-badge">
      <span class="logo-name">Velvet Corwin<br>Sauce</span>
    </div>
    <p class="tagline">Artisan Made - Small Batch</p>

    <h1 class="contact-name">Rory Whitlock<span class="title">, Creator</span></h1>
    <svg class="name-underline" width="212" height="14" viewBox="0 0 212 14" aria-hidden="true">
      <path d="M4 8 Q106 2 208 7" stroke="var(--brand-yellow)" stroke-width="4" fill="none" stroke-linecap="round"/>
    </svg>

    <p class="contact-line phone">
      <svg width="30" height="30" viewBox="0 0 24 24" aria-hidden="true">
        <circle cx="12" cy="12" r="10.5" fill="none" stroke="#fff" stroke-width="1.8"/>
        <path d="M8.6 6.8l1.6 2.4-1 1.2c.7 1.6 1.8 2.7 3.4 3.4l1.2-1 2.4 1.6-.9 2.1c-4.2-.4-8-4.2-8.4-8.4z" fill="#fff"/>
      </svg>
      123-456-7890
    </p>
    <p class="contact-line email">
      <svg width="28" height="22" viewBox="0 0 28 22" aria-hidden="true">
        <rect x="1" y="3" width="26" height="18" rx="2" fill="#fff"/>
        <path d="M2 5 L14 14 L26 5" stroke="var(--card-dark)" stroke-width="2" fill="none"/>
      </svg>
      rwhitlock@velvetcorwin.com
    </p>

    <div class="social">
      <span>Follow Us On</span>
      <span class="social-dots" aria-label="Social media links">
        <span class="social-dot"></span><span class="social-dot"></span><span class="social-dot"></span>
      </span>
    </div>

    <footer class="bottom-band">www.velvetcorwinsauce.com</footer>
  </main>
</body>
</html>
```